Redesign our company's business card. RVL BUSINESS CARD 2015

We are an Audio Visual Production company with a flare of marketing and sales. Lights camera ACTION!! We are Production and creative designers and thinkers whom provide first class service for many fortune 500 companies that Exhibit at trade shows and sales meetings.

Double sided, sleek, fashionable, and modern.

www.brightlanemedia.example

Think QRV'S Sidelines

Target Market(s)

Trade Show Mangers, Event coordinators, Project managers,

Industry/Entity Type

Marketing

Contact Information for Business Card

Name Tile, Logo, Slogan, photos of our work on the back. Facebook and twitter

Font styles to use
Sans Serif
Decorative
Script

Colors
33a6d7
ffffff
0692cd
cee9f5

Requirements
Must have
• Multi color, professional, Upscale,
• CREATING GREAT PARTNERSHIPS THAT PRODUCE AMAZING RESULTS
Nice to have
• Photos of our work on the back
Should not have
• Address or fax.

```html
<!DOCTYPE html>
<html lang="en">
<head>
<meta charset="utf-8">
<title>RVL Business Card</title>
<link rel="stylesheet" href="https://fonts.googleapis.com/css2?family=Cinzel:wght@400;600&display=swap">
<style>
  :root {
    --page: #ffffff;
    --card: #ffffff;
    --ink: #1b5e93;
    --wave-mid: #1a8fca;
    --wave-deep: #0b5a9a;
    --wave-light: #7dd2e0;
    --mark: #33a6d7;
    --photo-dark: #0d1420;
    --photo-glow: #2f7fc4;
  }
  html, body {
    margin: 0;
    width: 1200px;
    height: 1200px;
    overflow: hidden;
    background: var(--page);
  }
  .sheet {
    position: relative;
    width: 1200px;
    height: 1200px;
  }
  .card {
    position: absolute;
    background: var(--card);
    box-shadow: 6px 8px 10px rgba(0,0,0,0.28);
    overflow: hidden;
  }
  .card-front {
    left: 320px;
    top: 176px;
    width: 550px;
    height: 312px;
    outline: 1px solid #c8c8c8;
  }
  .card-back {
    left: 317px;
    top: 629px;
    width: 553px;
    height: 313px;
  }
  .brand {
    position: absolute;
    left: 122px;
    top: 24px;
    display: flex;
    align-items: center;
    gap: 18px;
  }
  .brand-dot {
    width: 88px;
    height: 88px;
    border-radius: 50%;
    background: var(--mark);
  }
  .brand-text {
    display: flex;
    flex-direction: column;
    font-family: "Cinzel", serif;
    font-weight: 600;
    color: var(--ink);
  }
  .brand-name {
    font-size: 52px;
    line-height: 1;
    letter-spacing: 2px;
  }
  .brand-full {
    font-size: 11px;
    letter-spacing: 1px;
    margin-top: 4px;
  }
  .slogan {
    position: absolute;
    left: 0;
    right: 0;
    top: 152px;
    text-align: center;
    font-family: "Cinzel", serif;
    font-weight: 600;
    color: var(--ink);
    margin: 0;
  }
  .slogan-main {
    display: block;
    font-size: 19px;
    letter-spacing: 0.6px;
  }
  .slogan-sub {
    display: block;
    font-size: 15px;
    margin-top: 5px;
    letter-spacing: 0.4px;
  }
  .waves {
    position: absolute;
    left: 0;
    top: 0;
    width: 550px;
    height: 312px;
  }
  .event-photo {
    width: 100%;
    height: 100%;
    background:
      radial-gradient(ellipse 45% 40% at 50% 55%, var(--photo-glow) 0%, rgba(47,127,196,0.35) 55%, transparent 80%),
      radial-gradient(ellipse 14% 22% at 8% 55%, #3d8fd6 0%, transparent 100%),
      radial-gradient(ellipse 16% 28% at 93% 48%, #3d8fd6 0%, transparent 100%),
      linear-gradient(180deg, #1a1f28 0%, var(--photo-dark) 60%, #07090d 100%);
  }
</style>
</head>
<body>
<main class="sheet">
  <section class="card card-front">
    <svg class="waves" viewBox="0 0 550 312" aria-hidden="true">
      <path fill="var(--wave-light)" d="M0,270 C140,300 300,250 550,248 L550,312 L0,312 Z"/>
      <path fill="#ffffff" d="M240,312 C330,285 440,265 550,262 L550,275 C450,280 350,295 290,312 Z"/>
      <path fill="var(--wave-mid)" d="M0,185 C110,165 200,240 320,222 C420,206 490,196 550,222 L550,242 C470,222 400,232 320,244 C200,262 100,262 0,258 Z"/>
      <path fill="var(--wave-deep)" d="M0,262 C140,292 300,232 550,238 L550,254 C300,244 150,302 0,286 Z"/>
    </svg>
    <div class="brand">
      <div class="brand-dot"></div>
      <div class="brand-text">
        <span class="brand-name">RVL</span>
        <span class="brand-full">Riverline Visual Labs</span>
      </div>
    </div>
    <p class="slogan">
      <span class="slogan-main">CREATING GREAT PARTNERSHIPS THAT</span>
      <span class="slogan-sub">PRODUCE AMAZING RESULTS</span>
    </p>
  </section>

  <section class="card card-back">
    <div class="event-photo" role="img" aria-label="Photo of a staged corporate event: presenter on a blue-lit stage with large side screens and a seated audience"></div>
  </section>
</main>
</body>
</html>
```